Kickass billboard for motorway

We take dented trucks - clue is in the name.
We have a 45ft billboard we're looking to design constructed from an old trailer we own (so we can be as creative as possible).
We provide a van buying service, being one of the only companies in the UK with the facilities to recover faulty, damaged and broken vans - from small car derived vans to large trucks and lorries.
ur niche in the market is different to car buying services, as buying and selling cars is often an emotionally driven process, whereas people often see and treat vans purely as a tool. There are alternatives to a car, public transport etc, but not to a work van - so people go out straight away and replace them immediately, often leaving the old broken van to sit on their drive or in their unit.
Looking to start building a brand asset bank.
Feel free to check out our website to get a feel for what we do:
Wetakedentedtrucks.co.uk

Target Market(s)

Van owners/drivers & fleet managers

Industry/Entity Type

Automotive

Font styles to use
Sans Serif

Colors
34a7d8

Requirements
Must have
• Eye-catching - very eye-catching.
We want to advertise the fact we collect vehicles for free.
We pay instantly upon arrival.
Our phone number 0161 473 2046
Our website www.wetakedentedtrucks.co.uk
Nice to have
• 3d elements - we have the ability to get 3d props for the billboard including damaged vans etc.

```html
<!DOCTYPE html>
<html lang="en">
<head>
<meta charset="utf-8">
<title>Wetakedentedtrucks.co.uk – Motorway Billboard</title>
<link href="https://fonts.googleapis.com/css2?family=Montserrat:wght@600;800&family=Oswald:wght@500;600&display=swap" rel="stylesheet">
<style>
  :root {
    --yellow: #ffea00;
    --blue: #0a5bc2;
    --black: #000000;
    --white: #ffffff;
    --stage: #e9edf1;
    --photo-light: #f4f5f6;
    --photo-mid: #c9ced4;
  }
  * { margin: 0; padding: 0; box-sizing: border-box; }
  html, body { width: 1200px; height: 1200px; overflow: hidden; }
  body { background: var(--stage); position: relative; }

  .billboard {
    position: absolute; left: 0; top: 400px;
    width: 1200px; height: 400px;
    overflow: hidden; background: var(--blue);
  }
  .billboard__shapes { position: absolute; inset: 0; }

  .truck-photo {
    position: absolute; left: 470px; top: 22px;
    width: 700px; height: 280px;
    border-radius: 40px 60px 30px 30px;
    background: radial-gradient(ellipse at 50% 45%, var(--photo-light) 0%, var(--photo-mid) 75%, rgba(201,206,212,0) 100%);
  }

  .headline {
    position: absolute; left: 34px; top: 28px;
    font-family: "Montserrat", sans-serif; text-transform: uppercase;
    line-height: 1;
  }
  .headline__small { font-weight: 600; font-size: 32px; color: var(--black); letter-spacing: 0.5px; }
  .headline__big { font-weight: 800; font-size: 60px; color: var(--blue); letter-spacing: -1px; }
  .headline__free { margin-top: 2px; }
  .headline__paid { margin-top: 24px; }
  .headline__arrival { margin-top: 4px; }

  .contact-band {
    position: absolute; left: 0; bottom: 0;
    width: 1200px; height: 90px;
    display: flex; align-items: center;
    font-family: "Oswald", sans-serif;
  }
  .phone { display: flex; align-items: center; margin-left: 34px; }
  .phone__cta {
    color: var(--yellow); font-weight: 500; font-size: 17px;
    line-height: 0.95; margin-right: 10px; text-transform: uppercase;
  }
  .phone__number { color: var(--white); font-weight: 600; font-size: 54px; letter-spacing: 1px; }

  .website { display: flex; align-items: center; margin-left: 44px; }
  .website__icon { width: 40px; height: 40px; margin-right: 14px; }
  .website__url { color: var(--white); font-weight: 600; font-size: 50px; letter-spacing: 2.5px; }
</style>
</head>
<body>
  <section class="billboard">
    <svg class="billboard__shapes" width="1200" height="400" viewBox="0 0 1200 400">
      <rect x="0" y="0" width="1200" height="400" fill="var(--blue)"/>
      <polygon points="0,0 640,0 440,310 0,310" fill="var(--yellow)"/>
      <polygon points="440,310 452,292 1200,292 1200,400 0,400 0,310" fill="var(--black)"/>
    </svg>

    <div class="truck-photo" role="img" aria-label="Photo of a white double-cab pickup truck, three-quarter front view"></div>

    <div class="headline">
      <p class="headline__small">We collect vehicles</p>
      <p class="headline__big headline__free">For free</p>
      <p class="headline__big headline__paid">Get paid</p>
      <p class="headline__big">Instantly</p>
      <p class="headline__small headline__arrival">Upon arrival</p>
    </div>

    <div class="contact-band">
      <div class="phone">
        <p class="phone__cta">Call<br>now!</p>
        <p class="phone__number">0161 473 2046</p>
      </div>
      <div class="website">
        <svg class="website__icon" viewBox="0 0 40 40" aria-hidden="true">
          <circle cx="20" cy="20" r="19" fill="var(--yellow)"/>
          <circle cx="20" cy="20" r="11" fill="none" stroke="var(--blue)" stroke-width="2"/>
          <ellipse cx="20" cy="20" rx="5" ry="11" fill="none" stroke="var(--blue)" stroke-width="2"/>
          <line x1="9" y1="20" x2="31" y2="20" stroke="var(--blue)" stroke-width="2"/>
        </svg>
        <p class="website__url">www.wetakedentedtrucks.co.uk</p>
      </div>
    </div>
  </section>
</body>
</html>
```